Relationship Dynamics and Development Self Help

Psychologist who will use the image as the foundational representation or framework for the prescriptive self help. The design will likely be used as the working model for the prescriptive help; but also could inform the logo for the materials or book cover. The artwork for the design must be able to appeal to a wide audience of females and males. I think a 4-leaf clover would be an awesome image to represent the content we intend to provide

Target Market(s)

couples seeking to improve their relationships - potentially more female clients than male

Industry/Entity Type

Psychology

Font styles to use
Sans Serif

Requirements
Must have
• colorful but representative of the tenet that all relationships are constant work. There are 4 types of relationships which i would like rendered as if a 4-leaf clover: Friendships, Companionships, Situationships, and Intimate Partnerships The clover shape must indicate (preferably with arrows) the these relationships can "flow into" one another--e.g, a friendship can become an intimate partnerships, etc.
Nice to have
• I think I'd like the clover to grow out of a ground that represents the nutrients that are necessary for it to grow
Should not have
• People that could imply there is a specific, preferred ethnicity or nationality for our help

```html
<!DOCTYPE html>
<html lang="en">
<head>
<meta charset="utf-8">
<title>Relationship Clover Framework</title>
<link rel="stylesheet" href="https://fonts.googleapis.com/css2?family=Roboto+Condensed:wght@700&display=swap">
<style>
  :root {
    --green: #3f962c;
    --green-light: #5ec243;
    --green-pale: #8fd97a;
    --blue: #2a7fbc;
    --blue-light: #3aa8ee;
    --blue-pale: #5bb8f5;
    --orange: #f19a17;
    --orange-light: #f0c013;
    --red: #c0392f;
    --red-light: #f0675a;
    --white: #ffffff;
    --bg: #ffffff;
  }
  html, body {
    margin: 0;
    padding: 0;
    width: 1200px;
    height: 912px;
    overflow: hidden;
    background: var(--bg);
  }
  .canvas {
    display: block;
    width: 1200px;
    height: 912px;
  }
  .label-text {
    font-family: "Roboto Condensed", "Arial Narrow", sans-serif;
    font-weight: 700;
    font-size: 42px;
    fill: var(--white);
    letter-spacing: 0.5px;
  }
  .ring-arc { fill: none; stroke-width: 12; stroke-linecap: butt; }
  .arc-green { stroke: var(--green); }
  .arc-blue { stroke: var(--blue-light); }
  .arc-orange { stroke: var(--orange); }
  .arc-red { stroke: var(--red); }
  .fill-green { fill: var(--green); }
  .fill-blue { fill: var(--blue); }
  .fill-orange { fill: var(--orange); }
  .fill-red { fill: var(--red); }
</style>
</head>
<body>
<svg class="canvas" viewBox="0 0 1920 1460" xmlns="http://www.w3.org/2000/svg">
  <defs>
    <path id="leaf-heart" d="M0 0 C -80 -80, -200 -180, -222 -280 C -245 -420, -100 -505, 0 -420 C 100 -505, 245 -420, 222 -280 C 200 -180, 80 -80, 0 0 Z"/>
    <polygon id="arrow-head" points="0,40 -42,-80 0,-52 42,-80"/>
    <linearGradient id="grad-green" x1="0" y1="0" x2="1" y2="0">
      <stop offset="0" stop-color="var(--green-pale)"/>
      <stop offset="0.5" stop-color="var(--green-light)"/>
      <stop offset="1" stop-color="var(--green-pale)"/>
    </linearGradient>
    <linearGradient id="grad-blue" x1="0" y1="0" x2="1" y2="0">
      <stop offset="0" stop-color="var(--blue)"/>
      <stop offset="0.5" stop-color="var(--blue-light)"/>
      <stop offset="1" stop-color="var(--blue-pale)"/>
    </linearGradient>
    <linearGradient id="grad-orange" x1="0" y1="0" x2="1" y2="0">
      <stop offset="0" stop-color="var(--orange-light)"/>
      <stop offset="0.5" stop-color="var(--orange)"/>
      <stop offset="1" stop-color="var(--orange-light)"/>
    </linearGradient>
    <linearGradient id="grad-red" x1="0" y1="0" x2="1" y2="0">
      <stop offset="0" stop-color="var(--red-light)"/>
      <stop offset="0.5" stop-color="var(--red)"/>
      <stop offset="1" stop-color="var(--red-light)"/>
    </linearGradient>
  </defs>

  <!-- Flow ring -->
  <g class="flow-ring">
    <path class="ring-arc arc-green" d="M588 330 A535 535 0 0 1 1332 330"/>
    <path class="ring-arc arc-blue" d="M1358 357 A535 535 0 0 1 1393 1030"/>
    <path class="ring-arc arc-orange" d="M1370 1059 A535 535 0 0 1 602 1113"/>
    <path class="ring-arc arc-red" d="M569 1080 A535 535 0 0 1 562 357"/>

    <use href="#arrow-head" class="fill-green" transform="translate(960 715) rotate(-42) translate(535 0)"/>
    <use href="#arrow-head" class="fill-blue" transform="translate(960 715) rotate(40) translate(535 0)"/>
    <use href="#arrow-head" class="fill-orange" transform="translate(960 715) rotate(137) translate(535 0)"/>
    <use href="#arrow-head" class="fill-red" transform="translate(960 715) rotate(226) translate(535 0)"/>
  </g>

  <!-- Clover leaves -->
  <g class="clover">
    <g class="leaf leaf-friendships" transform="translate(960 705)">
      <use href="#leaf-heart" fill="url(#grad-green)"/>
      <use href="#leaf-heart" class="fill-green" transform="translate(0 -22) scale(0.9)"/>
    </g>
    <g class="leaf leaf-companionships" transform="translate(970 715) rotate(90)">
      <use href="#leaf-heart" fill="url(#grad-blue)"/>
      <use href="#leaf-heart" class="fill-blue" transform="translate(0 -22) scale(0.9)"/>
    </g>
    <g class="leaf leaf-intimate" transform="translate(960 728) rotate(180)">
      <use href="#leaf-heart" fill="url(#grad-orange)"/>
      <use href="#leaf-heart" class="fill-orange" transform="translate(0 -22) scale(0.9)"/>
    </g>
    <g class="leaf leaf-situationships" transform="translate(950 715) rotate(-90)">
      <use href="#leaf-heart" fill="url(#grad-red)"/>
      <use href="#leaf-heart" class="fill-red" transform="translate(0 -22) scale(0.9)"/>
    </g>
  </g>

  <!-- Leaf pictograms -->
  <g class="leaf-icons">
    <rect role="img" aria-label="Pictogram of two friends standing side by side" x="880" y="345" width="165" height="215" rx="24" fill="var(--green-light)"/>
    <rect role="img" aria-label="Pictogram of two companions holding hands beneath a heart" x="1155" y="580" width="175" height="270" rx="24" fill="var(--blue-light)"/>
    <rect role="img" aria-label="Pictogram of two partners in a close embrace" x="895" y="855" width="140" height="220" rx="24" fill="var(--orange-light)"/>
    <rect role="img" aria-label="Pictogram of two open hands offering a heart" x="585" y="615" width="275" height="165" rx="24" fill="var(--red-light)"/>
  </g>

  <!-- Labels -->
  <g class="labels">
    <g class="label label-friendships">
      <rect x="804" y="145" width="312" height="68" rx="34" class="fill-green"/>
      <text class="label-text" x="960" y="194" text-anchor="middle">FRIENDSHIPS</text>
    </g>
    <g class="label label-companionships">
      <rect x="1459" y="518" width="66" height="395" rx="33" class="fill-blue"/>
      <text class="label-text" transform="translate(1478 715) rotate(90)" text-anchor="middle">COMPANIONSHIPS</text>
    </g>
    <g class="label label-situationships">
      <rect x="394" y="530" width="66" height="372" rx="33" class="fill-red"/>
      <text class="label-text" transform="translate(442 716) rotate(-90)" text-anchor="middle">SITUATIONSHIPS</text>
    </g>
    <g class="label label-intimate">
      <rect x="785" y="1218" width="350" height="106" rx="48" class="fill-orange"/>
      <text class="label-text" x="960" y="1262" text-anchor="middle">INTIMATE</text>
      <text class="label-text" x="960" y="1302" text-anchor="middle">PARTNERSHIPS</text>
    </g>
  </g>
</svg>
</body>
</html>
```